Personal Injury Attorney Marketing Brochure to Medical Providers

We are looking to have a brochure - booklet form - outside - inside and back page - to hand out to chiropractors, physical therapist, clinics and other medical providers that treat persons who were injured - from an auto accident - truck accident - slip and fall, work related injury. We want them to know we handle personal injury work and represent persons who were injured as a result of the negligence of another person / company. We want the brochure to be professional and represent that we have a lot of experience in this area - Brian in practice since 1990 and Lena since 2000. Please refer to our website - www.fenwoodlegal.com for the type of work that we do and the practice areas. If we need to send more content - let us know. The project is to advertise only Brian Tolliver and lena Moskos.
Updates

We added a QR code to add to the brochure

Target Market(s)

Medical providers - such as chiropractors, Physical therapist, orthopedic doctors who may be able to refer a patient to a personal injury attorney who can help them pursue a personal injury claim

Industry/Entity Type

We are personal injury attorneys - we represent persons who have been injured in car accidents, trucking accidents, work site accidents, slip and falls that result in - broken bones, serious injuries and other injuries to help them get compensation

Font styles to use
Serif

Colors
0054AA
0677BA
7BADD7
CADEEF
E8F1F8

Requirements
Must have
• Photos of law firm members Brian Tolliver and Lena Moskos and our firm logo, our l numnew location address - which is 415 Wexbury Mill Rd., Norcross, GA 30071 / our direct phone numbers / e-mail address / website and information about us and our practice / Free consult / Attorney's who are very accessible / We have spanish speaking attorney and staff members. Please use only LEXRA or Searchly reviews for Brian Tolliver or Lena Moskos - not for Gordon Pellish. For e-mail contact to the firm - add admin@fenwoodlegal or admin3@fenwoodlegal.com - and add for Spanish - 404-555-0172 or for English - 404-555-0186
Nice to have
• Quotes from satisfied customers from Brian Tolliver and Lena Moskos's Searchly reviews and LEXRA reviews / our LEXRA ratings - all of which can be found on the internet - or we can provide - see attached word document with Searchly and LEXRA review information.
Should not have
• No guarantee of results

```html
<!DOCTYPE html>
<html lang="en">
<head>
<meta charset="utf-8">
<title>Fenwood Legal – Injury Brochure</title>
<link rel="stylesheet" href="https://fonts.googleapis.com/css2?family=Quicksand:wght@400;500;700&family=Poppins:wght@300;400;500;600;700&display=swap">
<style>
:root{
  --blue-deep:#0054AA;
  --blue-mid:#0677BA;
  --blue-soft:#7BADD7;
  --blue-pale:#CADEEF;
  --blue-mist:#E8F1F8;
  --ink:#1f2430;
  --grey:#555b66;
  --paper:#ffffff;
  --star:#f5a623;
}
*{box-sizing:border-box;margin:0;padding:0}
html,body{width:1200px;height:1200px;overflow:hidden;background:#fff}
body{position:relative;font-family:"Poppins",sans-serif;color:var(--ink)}
.panel{position:absolute;background:var(--paper);box-shadow:0 2px 10px rgba(0,0,0,.18);overflow:hidden}

/* Cover */
.cover{left:199px;top:30px;width:379px;height:552px}
.cover__corner{position:absolute;left:0;top:0}
.brand{position:absolute;left:54px;top:30px;display:flex;align-items:center;gap:5px;font-family:"Quicksand",sans-serif;font-weight:700;font-size:12px;color:var(--ink)}
.brand__mark{width:9px;height:9px;background:var(--blue-deep)}
.cover__rule{position:absolute;left:210px;top:40px;width:169px;height:1px;background:var(--blue-deep)}
.cover__tag{position:absolute;right:36px;top:64px;font-size:6px;letter-spacing:.3px;color:var(--grey)}
.cover__title{position:absolute;right:35px;top:72px;text-align:right;font-family:"Quicksand",sans-serif}
.cover__title .l1{display:block;font-weight:700;font-size:27px;line-height:30px;color:#2a2a2a}
.cover__title .l2{display:block;background:var(--blue-mid);color:#fff;font-weight:500;font-size:25px;line-height:30px;padding:0 10px 0 14px;margin-right:-10px}
.cover__title .l3{display:block;font-weight:500;font-size:25px;line-height:32px;color:#2a2a2a}
.perks{position:absolute;left:138px;top:176px;font-size:7.6px;color:#333;line-height:14px}
.perks span{display:inline-flex;align-items:center;gap:5px;margin-right:8px}
.perks i{width:6px;height:6px;background:var(--blue-mid);display:inline-block}
.cover__art{position:absolute;left:0;top:226px}
.contact{position:absolute;left:0;top:450px;width:379px;height:102px;color:#fff}
.contact__addr{position:absolute;left:100px;top:26px;font-size:8.6px;line-height:12px;border-left:1px solid rgba(255,255,255,.7);padding-left:4px}
.contact__phone{position:absolute;left:257px;top:26px;font-size:8.6px;line-height:12px;border-left:1px solid rgba(255,255,255,.7);padding-left:4px}
.contact__pin{position:absolute;left:68px;top:29px}
.contact__tel{position:absolute;left:226px;top:29px}
.contact__mail{position:absolute;left:0;width:379px;top:68px;text-align:center;font-size:7px}
.contact__web{position:absolute;left:0;width:379px;top:79px;text-align:center;font-size:13px}

/* Reviews */
.reviews{left:620px;top:30px;width:378px;height:549px}
.reviews__head{position:absolute;left:0;top:0}
.reviews__title{position:absolute;right:42px;top:16px;text-align:right;color:#fff}
.reviews__title b{display:block;font-size:13.5px;font-weight:700;line-height:15px}
.reviews__title small{display:block;font-size:6.5px}
.biz{position:absolute;left:30px;top:64px}
.biz h3{font-weight:400;font-size:10.5px;color:#222}
.biz p{font-size:4.6px;color:#777}
.biz .score{font-size:11px;color:#555;margin-top:4px;display:flex;align-items:center;gap:4px}
.stars{color:var(--star);letter-spacing:.5px}
.biz .score .stars{font-size:10px}
.biz .score small{font-size:5px;color:#888}
.filters{position:absolute;left:30px;font-size:5px;color:#333}
.chips{display:flex;gap:3px;margin-top:5px}
.chip{border:1px solid #ccd3dc;border-radius:7px;padding:1px 5px;font-size:4.4px;color:#555}
.chip.on{background:var(--blue-mist);border-color:var(--blue-pale);color:var(--blue-deep)}
.review{position:absolute;left:30px;width:320px}
.review__avatar{position:absolute;left:0;top:0;width:13px;height:13px;border-radius:50%;color:#fff;font-size:7px;display:flex;align-items:center;justify-content:center}
.review__body{margin-left:20px}
.review__name{font-size:5.2px;font-weight:500;color:#222}
.review__meta{font-size:4.3px;color:#777}
.review__rate{font-size:4.5px;color:#777;margin-top:3px}
.review__rate .stars{font-size:6px}
.review__pos{font-size:4.6px;color:#555;margin-top:3px}
.review__text{font-size:4.6px;line-height:7.2px;color:#444;margin-top:5px}
.review__acts{font-size:4.4px;color:#777;margin-top:7px}

/* Inside spread */
.spread{left:199px;top:591px;width:799px;height:582px}
.spread__art{position:absolute;left:0;top:0}
.firm{position:absolute;left:29px;color:#fff}
.firm__kicker{top:258px;font-size:13px;font-weight:300}
.firm__title{top:272px;font-family:"Quicksand",sans-serif;font-weight:700;font-size:27px}
.firm__body{position:absolute;left:30px;top:316px;width:345px;font-size:7.2px;line-height:12px;color:#fff;font-weight:300}
.firm__more{position:absolute;left:30px;top:487px;width:345px;font-size:7.2px;line-height:12px;color:#444;font-weight:300}
.meet{position:absolute;right:30px;top:38px;text-align:right}
.meet__small{font-size:13px;font-weight:300;color:#444}
.meet__big{font-size:14px;font-weight:600;color:#333;letter-spacing:.3px}
.meet__rule{position:absolute;left:534px;top:90px;width:235px;height:1px;background:#777}
.meet__badges{position:absolute;right:30px;top:97px;font-size:13px;font-weight:300;color:#444}
.partner{position:absolute;top:368px;width:170px;text-align:center;color:#fff}
.partner h4{font-size:12.5px;font-weight:600;letter-spacing:.4px}
.partner p{font-size:10px;font-weight:300;color:rgba(255,255,255,.75)}
.partner__photo{position:absolute;left:25px;top:48px;width:120px;height:120px;border-radius:50%;border:4px solid #fff;box-shadow:0 0 0 1px var(--blue-pale)}
</style>
</head>
<body>

<!-- Front cover -->
<section class="panel cover">
  <svg class="cover__corner" width="40" height="64" viewBox="0 0 40 64"><polygon points="0,0 32,0 0,60" fill="var(--blue-deep)"/><line x1="32" y1="0" x2="48" y2="40" stroke="var(--blue-deep)" stroke-width="0.8"/></svg>
  <div class="brand"><span class="brand__mark"></span>Fenwood Legal</div>
  <div class="cover__rule"></div>
  <div class="cover__tag">DRIVEN. ATTENTIVE. RELIABLE.</div>
  <h1 class="cover__title">
    <span class="l1">Dedicated</span>
    <span class="l2">Georgia Injury</span>
    <span class="l3">Lawyers</span>
  </h1>
  <div class="perks">
    <div><span><i></i>Free consult</span><span><i></i>Attorney's who are very accessible</span></div>
    <div><span><i></i>We have spanish speaking attorney and staff members</span></div>
  </div>
  <svg class="cover__art" width="379" height="326" viewBox="0 0 379 326">
    <defs>
      <linearGradient id="coverBand" x1="0" y1="0" x2="1" y2="1">
        <stop offset="0" stop-color="var(--blue-soft)"/><stop offset="1" stop-color="var(--blue-deep)"/>
      </linearGradient>
      <linearGradient id="coverPhoto" x1="0" y1="0" x2="1" y2="1">
        <stop offset="0" stop-color="#b9a99a"/><stop offset=".5" stop-color="#6f6a6c"/><stop offset="1" stop-color="#3d4252"/>
      </linearGradient>
    </defs>
    <polygon points="0,96 56,0 379,0 379,326 0,326" fill="url(#coverBand)" opacity=".3"/>
    <polygon points="0,170 52,4 112,4 40,124 88,222 0,222" fill="var(--blue-mid)"/>
    <rect x="0" y="222" width="379" height="104" fill="url(#coverBand)"/>
    <polygon points="98,4 379,4 379,222 94,222 36,114" fill="#fff"/>
    <g role="img" aria-label="Photo of the two partners reviewing a case at a laptop in the office">
      <polygon points="104,9 379,9 379,218 98,218 42,114" fill="url(#coverPhoto)"/>
    </g>
  </svg>
  <div class="contact">
    <svg class="contact__pin" width="14" height="18" viewBox="0 0 14 18"><path d="M7 1a6 6 0 0 1 6 6c0 4.5-6 10-6 10S1 11.5 1 7a6 6 0 0 1 6-6z" fill="none" stroke="#fff" stroke-width="1.2"/><circle cx="7" cy="7" r="2.2" fill="none" stroke="#fff" stroke-width="1.2"/></svg>
    <div class="contact__addr">415 Wexbury Mill<br>Rd. Norcross, GA 30071</div>
    <svg class="contact__tel" width="18" height="18" viewBox="0 0 18 18"><path d="M4 2l3 3-1.6 2.2a9 9 0 0 0 5.4 5.4L13 11l3 3-2 2C8 16 2 10 2 4z" fill="none" stroke="#fff" stroke-width="1.2" stroke-linejoin="round"/></svg>
    <div class="contact__phone">(404) 555-0172<br>(404) 555-0186</div>
    <div class="contact__mail">admin@fenwoodlegal</div>
    <div class="contact__web">www.fenwoodlegal.com</div>
  </div>
</section>

<!-- Reviews page -->
<section class="panel reviews">
  <svg class="reviews__head" width="378" height="58" viewBox="0 0 378 58">
    <defs><linearGradient id="headGrad" x1="0" x2="1"><stop offset="0" stop-color="var(--blue-soft)"/><stop offset="1" stop-color="var(--blue-deep)"/></linearGradient></defs>
    <polygon points="0,0 378,0 339,58 0,58" fill="url(#headGrad)"/>
  </svg>
  <div class="reviews__title"><b>Searchly Reviews</b><small>for Lena and Brian</small></div>

  <div class="biz">
    <h3>Fenwood Legal, LLC</h3>
    <p>88 Larkmoor Pkwy NW #310, Norcross, GA</p>
    <div class="score">5.0 <span class="stars">★★★★★</span><small>19 reviews</small></div>
  </div>
  <div class="filters" style="top:112px">People often mention
    <div class="chips"><span class="chip on">All</span><span class="chip">call 5</span><span class="chip">results 4</span></div>
  </div>
  <div class="filters" style="top:142px">Sort by
    <div class="chips"><span class="chip on">Most relevant</span><span class="chip">Newest</span><span class="chip">Highest</span><span class="chip">Lowest</span></div>
  </div>

  <article class="review" style="top:186px">
    <div class="review__avatar" style="background:#a0522d" role="img" aria-label="Reviewer profile picture"></div>
    <div class="review__body">
      <div class="review__name">Tessa Whitcombe</div>
      <div class="review__meta">4 reviews · 1 photo</div>
      <div class="review__rate"><span class="stars">★★★★★</span> 4 days ago · NEW</div>
      <div class="review__pos"><b>Positive:</b> Professionalism, Quality, Responsiveness, Value</div>
      <p class="review__text">From my very first interaction with the firm, Lena and Marisol were extremely compassionate, friendly and set the bar for expectation. During the entire process, Lena kept me informed about next steps. She didn't mind answering my questions and made herself available to me whenever necessary. At the end of the day, if I needed to say anything about Lena, the team and the firm, simply put, one of the greatest decisions I made because I felt their authenticity about my well being and wasn't treated as another case number on their desk. Thank you, Fenwood Law.</p>
      <div class="review__acts">↰ Reply &nbsp;&nbsp; 👍 Like</div>
    </div>
  </article>

  <article class="review" style="top:298px">
    <div class="review__avatar" style="background:#455a64">A</div>
    <div class="review__body">
      <div class="review__name">April Vance</div>
      <div class="review__meta">1 review</div>
      <div class="review__rate"><span class="stars">★★★★★</span> 11 months ago</div>
      <div class="review__pos"><b>Positive:</b> Professionalism, Quality, Responsiveness, Value</div>
      <p class="review__text">Brian Tolliver represented my elderly mother in a rather complicated action and my family was extremely happy with the results. Brian expertly assessed her case at the outset and offered excellent advice at every juncture, guiding us to a very satisfactory conclusion.</p>
    </div>
  </article>

  <article class="review" style="top:391px">
    <div class="review__avatar" style="background:#8d6e63" role="img" aria-label="Reviewer profile picture"></div>
    <div class="review__body">
      <div class="review__name">Darnell Oakes</div>
      <div class="review__meta">1 review</div>
      <div class="review__rate"><span class="stars">★★★★★</span> 3 months ago</div>
      <div class="review__pos"><b>Positive:</b> Professionalism, Quality, Responsiveness, Value</div>
      <p class="review__text">Went to bat for me and kept me up to date on the process and the progress.</p>
    </div>
  </article>

  <article class="review" style="top:462px">
    <div class="review__avatar" style="background:#7e57c2">D</div>
    <div class="review__body">
      <div class="review__name">Dina Marsh</div>
      <div class="review__meta">2 reviews</div>
      <div class="review__rate"><span class="stars">★★★★★</span> a year ago</div>
      <p class="review__text">Lena helped me with my case and I couldn't have chosen a better attorney. She was very direct and stayed in contact with updates along the way. The end result I was very pleased and greatly appreciate Ms. Moskos for all her help!</p>
    </div>
  </article>
</section>

<!-- Inside spread -->
<section class="panel spread">
  <svg class="spread__art" width="799" height="582" viewBox="0 0 799 582">
    <defs>
      <linearGradient id="firmGrad" x1="0" y1="0" x2="1" y2="0.4">
        <stop offset="0" stop-color="var(--blue-soft)"/><stop offset=".55" stop-color="#4f8bcf"/><stop offset="1" stop-color="var(--blue-deep)"/>
      </linearGradient>
      <linearGradient id="teamPhoto" x1="0" y1="0" x2="0" y2="1">
        <stop offset="0" stop-color="#4d6a3a"/><stop offset=".55" stop-color="#6f6a62"/><stop offset="1" stop-color="#2e3440"/>
      </linearGradient>
      <linearGradient id="tailGrad" x1="0" x2="1">
        <stop offset="0" stop-color="var(--blue-pale)"/><stop offset="1" stop-color="var(--blue-soft)"/>
      </linearGradient>
    </defs>
    <polygon points="330,481 393,481 441,582 380,582" fill="url(#tailGrad)" opacity=".7"/>
    <polygon points="0,230 357,230 409,336 799,336 799,582 441,582 393,481 0,481" fill="url(#firmGrad)"/>
    <g role="img" aria-label="Group photo of the firm's three attorneys standing outdoors under trees">
      <polygon points="0,0 415,0 449,49 361,226 0,226" fill="url(#teamPhoto)"/>
    </g>
    <g role="img" aria-label="Attorney rating and membership badges">
      <rect x="460" y="160" width="76" height="64" rx="8" fill="var(--blue-mist)" stroke="var(--blue-pale)"/>
      <rect x="556" y="160" width="76" height="64" rx="8" fill="var(--blue-mist)" stroke="var(--blue-pale)"/>
      <rect x="652" y="160" width="76" height="64" rx="8" fill="var(--blue-mist)" stroke="var(--blue-pale)"/>
      <rect x="460" y="238" width="76" height="64" rx="8" fill="var(--blue-mist)" stroke="var(--blue-pale)"/>
      <rect x="556" y="238" width="76" height="64" rx="8" fill="var(--blue-mist)" stroke="var(--blue-pale)"/>
      <rect x="652" y="238" width="76" height="64" rx="8" fill="var(--blue-mist)" stroke="var(--blue-pale)"/>
    </g>
  </svg>

  <div class="firm firm__kicker">Meet</div>
  <div class="firm firm__title">Our Firm</div>
  <p class="firm__body">Dedicated to Accomplishing the Results You Want<br>
  At Fenwood Legal, LLC we are passionate about helping our injury clients achieve excellent results and recover the money they deserve. We have in-depth experience as trial attorneys defending insurance companies and their insureds. Because we have in the past dealt directly with claims representatives and insurance adjusters as our clients, we have unique insight into how insurance companies work and what they need to resolve cases at the maximum level possible.<br>
  We use this knowledge and put it to work for you, our client. Whether you were injured in a car accident, slip and fall, construction site accident, trucking accident, nursing home abuse or any other injury that was the fault of someone else, we are committed to pursuing the best result possible. If you have suffered an injury as the result of the negligence or fault of another person or company, rest assured that our attorneys will provide the knowledge and support you need to help you overcome this difficult time.</p>
  <p class="firm__more">Your attorneys work diligently to secure the facts and the evidence needed to maximize your compensation. If your case should proceed to trial, Fenwood is ready with decades of courtroom experience to fully present your case to the jury and pursue the best result possible in that setting. Should you decide to hire our lawyers, you will feel a peace of mind in knowing you have retained the services of an experienced, respected and reputable Georgia law firm. We build lasting relationships with our clients. Dependable. Attentive. Reliable. Fenwood.</p>

  <div class="meet">
    <div class="meet__small">Meet With</div>
    <div class="meet__big">BUSINESS PARTNER</div>
  </div>
  <div class="meet__rule"></div>
  <div class="meet__badges">Brian's badges</div>

  <div class="partner" style="left:436px">
    <h4>BRIAN TOLLIVER</h4><p>Partner</p>
    <div class="partner__photo" role="img" aria-label="Portrait of Brian Tolliver" style="background:radial-gradient(circle at 50% 40%,#a58a6e,#5a4a3c 70%,#2e2a30)"></div>
  </div>
  <div class="partner" style="left:610px">
    <h4>LENA MOSKOS</h4><p>Partner</p>
    <div class="partner__photo" role="img" aria-label="Portrait of Lena Moskos" style="background:radial-gradient(circle at 50% 40%,#c19a7a,#7a6454 70%,#3a3232)"></div>
  </div>
</section>

</body>
</html>
```